Courier Business needs a Business Card Design !!!

My new company needs a business card design. Our company name is Maple Dart Courier & Delivery Services. We will be servicing residential , government and business clients in the City of Yellowknife, Northwest Territories, Canada. I would like the following information included on the card: Name- Calvin Oxley. Title- Owner. Company- Maple Dart Courier & Delivery Services. Address- PO Box 5918 , Yellowknife , NWT, X0E 4K3. Phone- 867-555-0193. Email- mapledartdelivery@postfern.example. Facebook- www.socialpage.example/mapledartdelivery. I would like my double sided card to be the standard size of 84mm x 55mm. No borders. Use CMYK mode.1039x 697 pixels at least. I would like my logo to take up at least one quarter of the area of one side of the card. Text should be at least 8 point with perhaps my name being 10 point and my company name being 12-15 point . It should have clear readable font. Please use one or two bold colors. I am trying to attract the business community so a professional look might be best. My tag line is " On Time Every Time ". Nice safe margins please. We will be providing fast, reliable and professional delivery of envelopes and small packages within the City of Yellowknife. We offer 100% satisfaction or a complete refund. I have included a file of our logo. I like black, blue and red but am willing to look at what you feel would work best. I do not really like white as a background color.

Target Market(s)

Professionals , business owners. 30-50 years old

Industry/Entity Type

Residential

Contact Information for Business Card

As noted in brief

Font styles to use
Serif
Sans Serif

Colors
000000
0255a3
f04a50

Requirements
Must have
• My contact info. My logo
Nice to have
• Simple elegant design but still catches the eye
Should not have
• White background color

```html
<!DOCTYPE html>
<html lang="en">
<head>
<meta charset="utf-8">
<title>Maple Dart Courier &amp; Delivery Services – Business Card</title>
<link rel="stylesheet" href="https://fonts.googleapis.com/css2?family=Russo+One&family=Play:wght@400;700&display=swap">
<style>
  :root {
    --ink: #161616;
    --brand-blue: #0255a3;
    --brand-red: #f04a50;
    --paper: #ffffff;
    --backdrop: #5b5d60;
    --navy-text: #14213d;
  }
  * { box-sizing: border-box; margin: 0; padding: 0; }
  html, body { width: 1200px; height: 1000px; overflow: hidden; }
  body { background: var(--backdrop); position: relative; font-family: "Play", sans-serif; }

  .card { position: absolute; top: 127px; width: 500px; height: 763px; background: var(--paper); }
  .card--front { left: 95px; }
  .card--back { left: 615px; }
  .card__face {
    position: absolute; left: 27px; top: 27px; width: 446px; height: 708px;
    background: var(--brand-blue); border-radius: 10px; overflow: hidden;
  }

  /* Front */
  .holder-name {
    position: absolute; left: 104px; top: 120px;
    font-family: "Russo One", sans-serif; font-weight: 400; font-size: 60px; line-height: 58px;
    color: var(--ink); transform: rotate(3deg); transform-origin: left top;
  }
  .holder-name span { display: block; }
  .holder-name span + span { margin-left: 12px; }
  .runner-art { position: absolute; }
  .runner-art--left {
    left: 0; top: 286px; width: 84px; height: 106px;
    background: linear-gradient(90deg, #ffffff, #e4ecf6);
    border-radius: 0 38px 30px 0; opacity: .9;
  }
  .runner-art--right {
    left: 300px; top: 284px; width: 146px; height: 116px;
    background: linear-gradient(90deg, rgba(255,255,255,0) 0%, rgba(255,255,255,.6) 45%, #ffffff 75%);
    border-radius: 40px 0 0 30px;
  }
  .speed-line {
    position: absolute; left: 52px; top: 291px; width: 270px; height: 3px;
    background: linear-gradient(90deg, rgba(255,255,255,0), #ffffff);
  }
  .holder-title {
    position: absolute; left: 167px; top: 328px;
    font-family: "Russo One", sans-serif; font-size: 28px; color: var(--brand-red);
    transform: rotate(4deg);
  }
  .phone-box {
    position: absolute; left: 59px; top: 473px; width: 322px; height: 52px;
    background: var(--brand-red); border-radius: 6px;
    display: flex; align-items: center; justify-content: center;
    font-family: "Russo One", sans-serif; font-size: 26px; color: var(--paper); white-space: nowrap;
  }
  .contact-lines {
    position: absolute; left: 0; right: 0; top: 620px; text-align: center;
    color: var(--paper); font-size: 21px; line-height: 32px; letter-spacing: .3px; white-space: nowrap;
  }

  /* Back */
  .logo-plate { position: absolute; left: 69px; width: 310px; }
  .logo-plate--under { top: 58px; height: 340px; background: var(--paper); border-radius: 8px; transform: rotate(-5deg); }
  .logo-plate--top {
    top: 63px; height: 330px; background: var(--brand-red); border-radius: 10px; transform: rotate(7deg);
    display: flex; align-items: center; justify-content: center;
  }
  .wordmark {
    font-family: "Play", sans-serif; font-weight: 700;
    color: var(--ink); text-align: center; font-size: 23px; line-height: 30px;
    text-transform: uppercase; white-space: nowrap; transform: rotate(-7deg);
  }
  .company-lines {
    position: absolute; left: 0; right: 0; top: 450px; text-align: center;
    color: var(--paper); font-size: 25px; line-height: 32px; white-space: nowrap;
  }
  .address-lines {
    position: absolute; left: 0; right: 0; top: 544px; text-align: center;
    color: var(--navy-text); font-size: 25px; line-height: 31px; white-space: nowrap;
  }
  .tagline-band {
    position: absolute; left: 0; right: 0; top: 661px; height: 30px;
    background: var(--brand-red);
    display: flex; align-items: center; justify-content: center;
  }
  .tagline {
    font-family: "Play", sans-serif; font-weight: 400;
    font-size: 32px; line-height: 30px; letter-spacing: 1px;
    color: var(--brand-blue); white-space: nowrap; text-transform: uppercase;
  }
</style>
</head>
<body>
  <section class="card card--front">
    <div class="card__face">
      <h1 class="holder-name"><span>Calvin</span><span>Oxley</span></h1>
      <div class="speed-line"></div>
      <div class="runner-art runner-art--right" role="img" aria-label="Illustration of a running bird with speed lines"></div>
      <div class="runner-art runner-art--left" role="img" aria-label="Illustration of a running bird dashing off the card edge"></div>
      <p class="holder-title">owner</p>
      <p class="phone-box">Phone- 867-555-0193</p>
      <p class="contact-lines">mapledartdelivery@postfern.example<br>socialpage.example/mapledartdelivery</p>
    </div>
  </section>

  <section class="card card--back">
    <div class="card__face">
      <div class="logo-plate logo-plate--under"></div>
      <div class="logo-plate logo-plate--top">
        <p class="wordmark">Maple Dart<br>Courier &amp; Delivery Services</p>
      </div>
      <p class="company-lines">Maple Dart<br>Courier &amp; Delivery Services</p>
      <p class="address-lines">PO Box 5918 , Yellowknife<br>NWT, X0E 4K3</p>
      <div class="tagline-band"><p class="tagline">On Time Every Time</p></div>
    </div>
  </section>
</body>
</html>
```